Poster for Office

Looking for an edgy, beautiful poster to hang up in my office that uses the quotes located below and potentially the image attached.
Content for poster

Title: Pell's Rules

Must have the following quotes included (punctuation and capitalization are flexible, do what you think looks the best they also don't need the quotation symbols):

"Don't order fish at a steakhouse"
"Be bold. The more you tell, the more you sell"
"admit nothing, deny everything, launch counterattack."
"avoid obviousness"
"never do anything until you're ready to do it"
"look good=feel good"
"always keep the advantage"
"never complain, never explain"
"Lay low, play dumb, keep moving"

Industry/Entity Type

Quotes

Requirements
Must have
• Title: Pell's Rules

"avoid obviousness"
"look good=feel good"

```html
<!DOCTYPE html>
<html lang="en">
<head>
<meta charset="utf-8">
<title>Pell's Rules</title>
<link href="https://fonts.googleapis.com/css2?family=Leckerli+One&family=Roboto+Condensed:wght@400&display=swap" rel="stylesheet">
<style>
  :root {
    --frame: #12aee8;
    --sky-top: #8fd3f2;
    --sky-mid: #d8f0fb;
    --water: #c9e8f5;
    --ink: #0b0b0b;
    --navy: #143c74;
    --stone-dark: #1d232b;
    --stone-light: #58606b;
  }
  html, body { margin: 0; padding: 0; overflow: hidden; }
  .poster {
    position: relative;
    width: 848px;
    height: 1200px;
    box-sizing: border-box;
    border: 12px solid var(--frame);
    overflow: hidden;
    background: linear-gradient(180deg, var(--sky-top) 0%, #b6e2f6 30%, var(--sky-mid) 60%, #eef8fd 78%, var(--water) 100%);
  }
  .poster__glow {
    position: absolute;
    right: -60px; top: -60px;
    width: 420px; height: 420px;
    background: radial-gradient(circle, rgba(255,255,255,0.85) 0%, rgba(255,255,255,0) 70%);
  }
  .stone-stack {
    position: absolute;
    left: 390px; top: 770px;
    width: 446px; height: 418px;
    background: radial-gradient(ellipse 55% 50% at 55% 55%, var(--stone-light) 0%, var(--stone-dark) 60%, rgba(29,35,43,0) 100%);
  }
  .title {
    position: absolute;
    left: 92px; top: 128px;
    margin: 0;
    font-family: "Leckerli One", cursive;
    font-weight: 400;
    font-size: 82px;
    line-height: 1;
    color: var(--ink);
    transform: rotate(-21deg);
    transform-origin: 0 100%;
    white-space: nowrap;
    text-decoration: underline;
    text-decoration-thickness: 4px;
    text-underline-offset: 10px;
  }
  .rules {
    list-style: none;
    margin: 0; padding: 0;
    font-family: "Roboto Condensed", sans-serif;
    font-size: 30px;
    line-height: 1;
  }
  .rule {
    position: absolute;
    transform: rotate(-17deg);
    transform-origin: 0 100%;
    white-space: nowrap;
    color: var(--ink);
  }
  .rule::before { content: "\2022\00a0"; }
  .rule--accent { color: var(--navy); }
  .rule__cont { display: block; padding-left: 16px; }
</style>
</head>
<body>
<div class="poster">
  <div class="poster__glow"></div>
  <div class="stone-stack" role="img" aria-label="Stack of smooth dark balancing stones rising from still water with ripples"></div>

  <h1 class="title">Pell's Rules</h1>

  <ul class="rules">
    <li class="rule" style="left:52px; top:302px;">Don't order fish at a steakhouse</li>
    <li class="rule rule--accent" style="left:72px; top:360px;">Be bold. The more you tell, the more you sell</li>
    <li class="rule" style="left:92px; top:452px;">Admit nothing, deny everything,<span class="rule__cont">launch counterattack</span></li>
    <li class="rule rule--accent" style="left:120px; top:524px;">Avoid obviousness</li>
    <li class="rule" style="left:138px; top:586px;">Never do anything until you're ready to do it</li>
    <li class="rule rule--accent" style="left:158px; top:644px;">Look good=Feel good</li>
    <li class="rule" style="left:176px; top:704px;">Always keep the advantage</li>
    <li class="rule rule--accent" style="left:196px; top:764px;">Never complain, never explain</li>
    <li class="rule" style="left:214px; top:824px;">Lay low, play dumb, keep moving</li>
  </ul>
</div>
</body>
</html>
```